Menu Board 1000mmx500mm re-design

I would like to re-design exiting menu board 1000mmx500mm. Current board letters are bit to small to read. I would like to have pictures (attached) of the food offered on it and at the same time to create balance between pictures and size of the text to be easily readable. Fonts and colours are up to designer choice but prefer warm and bright colours rather anything dark.

Target Market(s)

Food industry

Industry/Entity Type

Food

Font styles to use
Other font styles liked:
• I leave font choice to designer

Colors
FFC000
F8CF3A
FAE287
FDF2CF
FEFAEE
F0912C
F2A743
F7CA91
FBE8D2
FDF5EE
EE7325
F08F49
F5BC92
FAE3D3
FDF4ED

Requirements
Must have
• Pictures + Text
Nice to have
• Balance between images and text.
Should not have
• Can't think of any

```html
<!DOCTYPE html>
<html lang="en">
<head>
<meta charset="utf-8">
<title>Menu Board</title>
<link href="https://fonts.googleapis.com/css2?family=Permanent+Marker&family=Roboto:wght@400;700&display=swap" rel="stylesheet">
<style>
  :root {
    --orange: #EE7325;
    --orange-deep: #E8621C;
    --orange-light: #F0912C;
    --yellow: #FFC000;
    --label-yellow: #FFCC00;
    --label-text: #E8441C;
    --paper: #F1F1F1;
    --ink: #2B2B2B;
    --sauce-ink: #3A1E0C;
    --backdrop: #D6D6D6;
    --white: #FFFFFF;
  }
  * { margin: 0; padding: 0; box-sizing: border-box; }
  html, body { width: 710px; height: 1200px; overflow: hidden; }
  body { background: var(--backdrop); position: relative; font-family: "Roboto", Arial, sans-serif; }

  .board { position: absolute; left: 55px; top: 0; width: 600px; height: 1200px; background: var(--paper); overflow: hidden; }

  .hero { position: absolute; left: 0; top: 0; width: 600px; height: 600px; }

  .menu-title {
    position: absolute; left: 0; width: 600px; top: 395px; text-align: center;
    font-family: "Permanent Marker", cursive; font-size: 72px; line-height: 1;
    color: var(--orange); letter-spacing: -1px;
  }

  .dish { position: absolute; width: 182px; text-align: center; }
  .dish-photo-ring {
    position: relative; margin: 0 auto; width: 140px; height: 140px; border-radius: 50%;
    border: 2px dashed var(--orange); padding: 6px;
  }
  .dish-photo {
    width: 124px; height: 124px; border-radius: 50%; border: 5px solid var(--orange-light);
  }
  .price { position: absolute; right: -14px; top: -16px; width: 50px; height: 50px; }
  .price svg, .drink-badge svg { position: absolute; inset: 0; width: 100%; height: 100%; }
  .price span, .drink-badge span {
    position: relative; display: flex; align-items: center; justify-content: center; height: 100%;
    color: var(--white); font-weight: 700;
  }
  .price span { font-size: 17px; }
  .dish-name {
    margin: 12px auto 0; width: 167px; height: 34px; background: var(--label-yellow);
    border-radius: 12px 2px 12px 2px;
    font-family: "Permanent Marker", cursive; font-size: 16px; line-height: 36px; color: var(--label-text);
  }
  .dish-desc { margin-top: 9px; font-size: 12.5px; line-height: 15.5px; color: var(--ink); }

  .drinks { position: absolute; left: 0; top: 1015px; width: 600px; height: 100px; }
  .drink-badge { position: absolute; width: 100px; height: 68px; }
  .drink-badge span { flex-direction: column; font-size: 15px; line-height: 1.1; }
  .drink-badge small { font-family: "Permanent Marker", cursive; font-weight: 400; font-size: 11px; color: var(--yellow); }
  .drink-photo { position: absolute; }

  .sauces {
    position: absolute; left: 0; bottom: 0; width: 600px; height: 52px; background: var(--orange-deep);
    display: flex; align-items: center; padding-left: 30px; font-weight: 700; white-space: nowrap;
  }
  .sauces-edge { position: absolute; left: 0; top: -6px; width: 600px; height: 8px; }
  .sauces-title { color: var(--white); font-size: 20px; margin-right: 14px; }
  .sauce { color: var(--sauce-ink); font-size: 14.5px; }
  .sauce + .sauce::before { content: "|"; font-weight: 400; margin: 0 6px; color: var(--sauce-ink); }
</style>
</head>
<body>
<main class="board">

  <svg class="hero" viewBox="0 0 600 600" aria-hidden="false">
    <defs>
      <linearGradient id="potatoTone" x1="0" y1="0" x2="1" y2="1">
        <stop offset="0" stop-color="#C98A2A"/><stop offset="0.5" stop-color="#E7A93A"/><stop offset="1" stop-color="#8E5A1E"/>
      </linearGradient>
      <linearGradient id="wrapTone" x1="0" y1="0" x2="0" y2="1">
        <stop offset="0" stop-color="#D9CFB8"/><stop offset="0.5" stop-color="#6F8F3C"/><stop offset="1" stop-color="#B9452E"/>
      </linearGradient>
      <linearGradient id="chickenTone" x1="0" y1="0" x2="1" y2="1">
        <stop offset="0" stop-color="#E4B77A"/><stop offset="0.5" stop-color="#F1E6D2"/><stop offset="1" stop-color="#7A4A22"/>
      </linearGradient>
    </defs>
    <polygon role="img" aria-label="Photo of roasted potatoes with thyme" points="0,0 300,280 0,560" fill="url(#potatoTone)"/>
    <polygon role="img" aria-label="Photo of a grilled veggie wrap cut in half" points="0,0 600,0 300,280" fill="url(#wrapTone)"/>
    <polygon role="img" aria-label="Photo of roast chicken with rice" points="600,0 600,565 300,280" fill="url(#chickenTone)"/>
    <g stroke-linecap="butt">
      <line x1="-10" y1="-10" x2="610" y2="575" stroke="var(--white)" stroke-width="52"/>
      <line x1="-10" y1="570" x2="610" y2="-10" stroke="var(--white)" stroke-width="52"/>
      <line x1="-10" y1="-10" x2="610" y2="575" stroke="var(--orange)" stroke-width="30"/>
      <line x1="-10" y1="570" x2="610" y2="-10" stroke="var(--orange)" stroke-width="30"/>
    </g>
    <circle cx="300" cy="281" r="34" fill="var(--orange)"/>
    <path d="M0,578 L300,300 L600,582 L600,600 L0,600 Z" fill="var(--paper)"/>
  </svg>

  <h1 class="menu-title">MENU</h1>

  <!-- Row one -->
  <section class="dish" style="left:19px; top:517px;">
    <div class="dish-photo-ring">
      <div class="dish-photo" role="img" aria-label="Photo of a chicken ciabatta with rocket" style="background:radial-gradient(circle at 50% 45%, #E3C28B, #5B8A2E 55%, #6B4425);"></div>
      <div class="price"><svg viewBox="-32 -32 64 64"><polygon fill="var(--orange)" points="32,0 24.1,6.5 27.7,16 17.7,17.7 16,27.7 6.5,24.1 0,32 -6.5,24.1 -16,27.7 -17.7,17.7 -27.7,16 -24.1,6.5 -32,0 -24.1,-6.5 -27.7,-16 -17.7,-17.7 -16,-27.7 -6.5,-24.1 0,-32 6.5,-24.1 16,-27.7 17.7,-17.7 27.7,-16 24.1,-6.5"/></svg><span>£6</span></div>
    </div>
    <h2 class="dish-name">CIABATTA</h2>
    <p class="dish-desc">Roti Chicken, Rucola,<br>Caramelized onions,Tomato,<br>Fresh Onion</p>
  </section>

  <section class="dish" style="left:201px; top:517px;">
    <div class="dish-photo-ring">
      <div class="dish-photo" role="img" aria-label="Photo of a grilled chicken wrap with slaw" style="background:radial-gradient(circle at 50% 45%, #F2E6CF, #B88EB0 55%, #8A5A33);"></div>
      <div class="price"><svg viewBox="-32 -32 64 64"><polygon fill="var(--orange)" points="32,0 24.1,6.5 27.7,16 17.7,17.7 16,27.7 6.5,24.1 0,32 -6.5,24.1 -16,27.7 -17.7,17.7 -27.7,16 -24.1,6.5 -32,0 -24.1,-6.5 -27.7,-16 -17.7,-17.7 -16,-27.7 -6.5,-24.1 0,-32 6.5,-24.1 16,-27.7 17.7,-17.7 27.7,-16 24.1,-6.5"/></svg><span>£7</span></div>
    </div>
    <h2 class="dish-name">WRAP</h2>
    <p class="dish-desc">Roti Chicken, Crunchy Slaw,<br>Tomato, Fresh Onion<br>&amp; Sauce of your choice</p>
  </section>

  <section class="dish" style="left:382px; top:517px;">
    <div class="dish-photo-ring">
      <div class="dish-photo" role="img" aria-label="Photo of a beetroot wrap with chicken and salad" style="background:radial-gradient(circle at 50% 50%, #D9D3C4, #6E9A48 50%, #8E2E45);"></div>
      <div class="price"><svg viewBox="-32 -32 64 64"><polygon fill="var(--orange)" points="32,0 24.1,6.5 27.7,16 17.7,17.7 16,27.7 6.5,24.1 0,32 -6.5,24.1 -16,27.7 -17.7,17.7 -27.7,16 -24.1,6.5 -32,0 -24.1,-6.5 -27.7,-16 -17.7,-17.7 -16,-27.7 -6.5,-24.1 0,-32 6.5,-24.1 16,-27.7 17.7,-17.7 27.7,-16 24.1,-6.5"/></svg><span>£8</span></div>
    </div>
    <h2 class="dish-name">BEETROOT WRAP</h2>
    <p class="dish-desc">Roti Chicken, Crunchy Slaw,<br>Tomato, Fresh Onion &amp;<br>Sauce of your choice</p>
  </section>

  <!-- Row two -->
  <section class="dish" style="left:19px; top:781px;">
    <div class="dish-photo-ring">
      <div class="dish-photo" role="img" aria-label="Photo of a quarter roast chicken with veggie rice" style="background:linear-gradient(90deg, #B07A45 0%, #C99258 50%, #F1ECDD 60%, #EDE6CF 100%);"></div>
      <div class="price"><svg viewBox="-32 -32 64 64"><polygon fill="var(--orange)" points="32,0 24.1,6.5 27.7,16 17.7,17.7 16,27.7 6.5,24.1 0,32 -6.5,24.1 -16,27.7 -17.7,17.7 -27.7,16 -24.1,6.5 -32,0 -24.1,-6.5 -27.7,-16 -17.7,-17.7 -16,-27.7 -6.5,-24.1 0,-32 6.5,-24.1 16,-27.7 17.7,-17.7 27.7,-16 24.1,-6.5"/></svg><span>£9</span></div>
    </div>
    <h2 class="dish-name">1/4 CHICKEN BOX</h2>
    <p class="dish-desc">Roti Chicken,<br>Veggie Rice &amp; Salad</p>
  </section>

  <section class="dish" style="left:201px; top:781px;">
    <div class="dish-photo-ring">
      <div class="dish-photo" role="img" aria-label="Photo of a half roast chicken with veggie rice" style="background:linear-gradient(90deg, #A8692E 0%, #C78A45 50%, #F1ECDD 62%, #EDE6CF 100%);"></div>
      <div class="price"><svg viewBox="-32 -32 64 64"><polygon fill="var(--orange)" points="32,0 24.1,6.5 27.7,16 17.7,17.7 16,27.7 6.5,24.1 0,32 -6.5,24.1 -16,27.7 -17.7,17.7 -27.7,16 -24.1,6.5 -32,0 -24.1,-6.5 -27.7,-16 -17.7,-17.7 -16,-27.7 -6.5,-24.1 0,-32 6.5,-24.1 16,-27.7 17.7,-17.7 27.7,-16 24.1,-6.5"/></svg><span>£14</span></div>
    </div>
    <h2 class="dish-name">1/2 CHICKEN BOX</h2>
    <p class="dish-desc">Roti Chicken,<br>Veggie Rice &amp; Salad</p>
  </section>

  <section class="dish" style="left:382px; top:781px;">
    <div class="dish-photo-ring">
      <div class="dish-photo" role="img" aria-label="Photo of roasted potatoes with thyme and garlic" style="background:radial-gradient(circle at 55% 50%, #F2C45A, #D8902A 60%, #8A521C);"></div>
      <div class="price"><svg viewBox="-32 -32 64 64"><polygon fill="var(--orange)" points="32,0 24.1,6.5 27.7,16 17.7,17.7 16,27.7 6.5,24.1 0,32 -6.5,24.1 -16,27.7 -17.7,17.7 -27.7,16 -24.1,6.5 -32,0 -24.1,-6.5 -27.7,-16 -17.7,-17.7 -16,-27.7 -6.5,-24.1 0,-32 6.5,-24.1 16,-27.7 17.7,-17.7 27.7,-16 24.1,-6.5"/></svg><span>£2.5</span></div>
    </div>
    <h2 class="dish-name">ROASTED POTATOS</h2>
    <p class="dish-desc">Thyme &amp; Garlic</p>
  </section>

  <!-- Drinks -->
  <section class="drinks">
    <div class="drink-badge" style="left:81px; top:20px;">
      <svg viewBox="-32 -32 64 64" preserveAspectRatio="none"><polygon fill="var(--orange)" points="32,0 24.1,6.5 27.7,16 17.7,17.7 16,27.7 6.5,24.1 0,32 -6.5,24.1 -16,27.7 -17.7,17.7 -27.7,16 -24.1,6.5 -32,0 -24.1,-6.5 -27.7,-16 -17.7,-17.7 -16,-27.7 -6.5,-24.1 0,-32 6.5,-24.1 16,-27.7 17.7,-17.7 27.7,-16 24.1,-6.5"/></svg>
      <span><small>WATER CAN</small>£1</span>
    </div>
    <div class="drink-photo" role="img" aria-label="Photo of a water bottle and a glass of water" style="left:201px; top:12px; width:65px; height:84px; border-radius:8px; background:linear-gradient(180deg, #CFE3F3, #6FA6D6);"></div>
    <div class="drink-badge" style="left:288px; top:20px;">
      <svg viewBox="-32 -32 64 64" preserveAspectRatio="none"><polygon fill="var(--orange)" points="32,0 24.1,6.5 27.7,16 17.7,17.7 16,27.7 6.5,24.1 0,32 -6.5,24.1 -16,27.7 -17.7,17.7 -27.7,16 -24.1,6.5 -32,0 -24.1,-6.5 -27.7,-16 -17.7,-17.7 -16,-27.7 -6.5,-24.1 0,-32 6.5,-24.1 16,-27.7 17.7,-17.7 27.7,-16 24.1,-6.5"/></svg>
      <span><small>JUICES</small>£1.8</span>
    </div>
    <div class="drink-photo" role="img" aria-label="Photo of fresh juices with orange, kiwi and tomato" style="left:400px; top:2px; width:120px; height:91px; border-radius:8px; background:linear-gradient(90deg, #F29A1E, #8CC63F 45%, #D9263B);"></div>
  </section>

  <footer class="sauces">
    <svg class="sauces-edge" viewBox="0 0 600 8" preserveAspectRatio="none" aria-hidden="true"><path d="M0,8 L0,4 L40,2 L90,5 L150,1 L220,4 L290,2 L360,5 L430,1 L500,4 L560,2 L600,4 L600,8 Z" fill="var(--orange-deep)"/></svg>
    <span class="sauces-title">SAUCES:</span>
    <span class="sauce">SIGNATURE</span><span class="sauce">BBQ</span><span class="sauce">PIRI PIRI</span><span class="sauce">SWEET CHILLI</span><span class="sauce">GARLIC MAYO</span>
  </footer>

</main>
</body>
</html>
```